50 bday

It's my 50th bday and I need the invitation that we will be send by digital (mail and whatapp). One important aspect is that my bday is on day 2 month 2 of year 22 so this is going to be important things that I want to use it as the main theme as you can see in the attached example

```html
<!DOCTYPE html>
<html lang="en">
<head>
<meta charset="utf-8">
<title>50th Birthday Invitation</title>
<link rel="stylesheet" href="https://fonts.googleapis.com/css2?family=Philosopher:wght@700&family=Yellowtail&family=DM+Serif+Display&family=Montserrat:wght@700&family=Alegreya+Sans:wght@500&display=swap">
<style>
  :root {
    --page: #ffffff;
    --green: #0d5a25;
    --green-deep: #0a4a1e;
    --green-glow: #146b2f;
    --silver: #e9e9ea;
    --gold: #e6b73a;
    --gold-dark: #a37a15;
    --day: #f3915f;
    --day-shade: #c8653a;
    --month: #2f98ec;
    --month-shade: #1a6dbb;
    --year: #f1c11c;
    --year-shade: #bf8f08;
    --band: #000000;
    --white: #ffffff;
  }
  html, body {
    margin: 0;
    padding: 0;
    width: 1200px;
    height: 1200px;
    overflow: hidden;
    background: var(--page);
  }
  .canvas {
    position: relative;
    width: 1200px;
    height: 1200px;
  }
  .invitation {
    position: absolute;
    left: 151px;
    top: 301px;
    width: 900px;
    height: 599px;
    overflow: hidden;
    background: radial-gradient(ellipse at 50% 55%, var(--green-glow) 0%, var(--green) 55%, var(--green-deep) 100%);
  }
  .confetti {
    position: absolute;
    top: 0;
    width: 210px;
    height: 190px;
  }
  .confetti--left {
    left: 0;
    background: radial-gradient(ellipse at 0% 0%, rgba(230,183,58,0.35) 0%, rgba(230,183,58,0) 70%);
  }
  .confetti--right {
    right: 0;
    background: radial-gradient(ellipse at 100% 0%, rgba(230,183,58,0.35) 0%, rgba(230,183,58,0) 70%);
  }
  .kicker {
    position: absolute;
    left: 0;
    right: 0;
    top: 35px;
    margin: 0;
    text-align: center;
    font-family: "Philosopher", sans-serif;
    font-weight: 700;
    font-size: 45px;
    color: var(--silver);
    letter-spacing: 0.5px;
    text-shadow: 0 2px 3px rgba(0,0,0,0.35);
  }
  .headline {
    position: absolute;
    left: 0;
    right: 0;
    top: 92px;
    margin: 0;
    text-align: center;
    font-family: "Yellowtail", cursive;
    font-weight: 400;
    font-size: 76px;
    color: var(--gold);
    text-shadow: 0 2px 0 var(--gold-dark), 0 4px 6px rgba(0,0,0,0.35);
  }
  .headline sup {
    font-size: 0.55em;
    vertical-align: 0.7em;
    margin-right: 6px;
  }
  .date {
    position: absolute;
    left: 0;
    top: 160px;
    width: 900px;
    height: 300px;
  }
  .digit {
    position: absolute;
    top: 0;
    width: 200px;
    margin-left: -100px;
    text-align: center;
    font-family: "DM Serif Display", serif;
    font-size: 330px;
    line-height: 300px;
  }
  .digit--day { left: 175px; color: var(--day); text-shadow: 0 3px 0 var(--day-shade), 0 6px 0 var(--day-shade), 0 10px 12px rgba(0,0,0,0.45); }
  .digit--month { left: 358px; color: var(--month); text-shadow: 0 3px 0 var(--month-shade), 0 6px 0 var(--month-shade), 0 10px 12px rgba(0,0,0,0.45); }
  .digit--year-a { left: 540px; color: var(--year); text-shadow: 0 3px 0 var(--year-shade), 0 6px 0 var(--year-shade), 0 10px 12px rgba(0,0,0,0.45); }
  .digit--year-b { left: 721px; color: var(--year); text-shadow: 0 3px 0 var(--year-shade), 0 6px 0 var(--year-shade), 0 10px 12px rgba(0,0,0,0.45); }
  .label {
    position: absolute;
    font-family: "Montserrat", sans-serif;
    font-weight: 700;
    font-size: 22px;
    letter-spacing: 0.5px;
    transform: translate(-50%, -50%) rotate(-47deg);
    text-shadow: 0 2px 3px rgba(0,0,0,0.4);
  }
  .label--day { left: 125px; top: 160px; color: var(--day); }
  .label--month { left: 316px; top: 156px; color: var(--month); }
  .label--year { left: 498px; top: 156px; color: var(--year); }
  .message {
    position: absolute;
    left: 0;
    bottom: 0;
    width: 900px;
    height: 123px;
    background: var(--band);
    display: flex;
    flex-direction: column;
    justify-content: center;
    align-items: center;
    font-family: "Alegreya Sans", sans-serif;
    font-weight: 500;
    font-size: 27px;
    line-height: 36px;
    text-transform: uppercase;
  }
  .message p { margin: 0; }
  .message__lead { color: var(--white); }
  .message__accent { color: var(--gold); }
</style>
</head>
<body>
<div class="canvas">
  <section class="invitation">
    <div class="confetti confetti--left" role="img" aria-label="Gold curling confetti ribbons"></div>
    <div class="confetti confetti--right" role="img" aria-label="Gold curling confetti ribbons"></div>

    <p class="kicker">Invitation To My</p>
    <h1 class="headline">50<sup>th</sup>Birthday Celebration</h1>

    <div class="date" aria-label="Date: day 2, month 2, year 22">
      <span class="digit digit--day">2</span>
      <span class="digit digit--month">2</span>
      <span class="digit digit--year-a">2</span>
      <span class="digit digit--year-b">2</span>
      <span class="label label--day">DAY</span>
      <span class="label label--month">MONTH</span>
      <span class="label label--year">YEAR</span>
    </div>

    <div class="message">
      <p class="message__lead">Reserva desde ahora ese día en tu agenda para</p>
      <p class="message__accent">Juntos compartir en la celebración de mis 50 años</p>
    </div>
  </section>
</div>
</body>
</html>
```